Marlow Estate Services (Handyman / Home Improvement Company)

Looking for a double sided professional looking business card with Logo attached to be highlighted on one side and throwing in an image of a handyman as an option would be nice to see as well. We are a company focused on providing quality Handyman and Home improvement services in a timely manner that is done right the first time with integrity

Industry/Entity Type

Handyman / Home Improvement

Contact Information for Business Card

(LOGO, Name, Mobile and office phone numbers, email) on front side of card, (the words "The SOLUTION to all of your Handyman and Home Improvement needs" followed by "Family Owned and Operated" at the very bottom) on the back.

Colors
EB3D1F
EC4F4E
F09395
F8D3D4
FCEDEE

Requirements
Must have
• Red, Gray, Black Color scheme
Should not have
• No Yellow or Blue colors

```html
<!DOCTYPE html>
<html lang="en">
<head>
<meta charset="utf-8">
<title>Marlow Estate Services – Business Card</title>
<link href="https://fonts.googleapis.com/css2?family=Montserrat:wght@400;500;600;700&display=swap" rel="stylesheet">
<style>
  :root {
    --backdrop: #9b9b9b;
    --card: #151515;
    --red: #e5302f;
    --white: #f4f4f4;
    --silver: #b9b9b9;
  }
  * { margin: 0; padding: 0; box-sizing: border-box; }
  html, body {
    width: 1200px; height: 1108px; overflow: hidden;
    background: var(--backdrop);
    font-family: "Montserrat", sans-serif;
  }
  .card {
    position: absolute;
    left: 242px; width: 715px; height: 408px;
    background: var(--card);
    border-radius: 30px;
    color: var(--white);
  }
  .card--cover { top: 119px; }
  .card--contact { top: 580px; }

  .tagline {
    position: absolute; top: 29px; left: 0; right: 0;
    text-align: center; font-weight: 600; font-size: 16.6px; letter-spacing: 0.1px;
  }
  .wordmark {
    position: absolute; display: flex; align-items: center; gap: 14px;
    font-weight: 700; text-transform: uppercase; line-height: 1.05;
  }
  .wordmark__dot { flex: none; border-radius: 50%; }
  .card--cover .wordmark {
    left: 0; right: 0; top: 150px; justify-content: center;
    color: var(--silver); font-size: 40px; text-align: left;
  }
  .card--cover .wordmark__dot { width: 22px; height: 22px; background: var(--silver); }
  .motto {
    position: absolute; bottom: 25px; left: 0; right: 0;
    text-align: center; font-size: 17px; font-weight: 400; letter-spacing: 0.4px;
  }

  .card--contact .wordmark {
    left: 40px; top: 160px; width: 270px;
    color: var(--white); font-size: 30px;
  }
  .card--contact .wordmark__dot { width: 20px; height: 20px; background: var(--red); }
  .divider {
    position: absolute; left: 325px; top: 82px; width: 2px; height: 243px;
    background: var(--red);
  }
  .details { position: absolute; left: 351px; top: 78px; }
  .details__name {
    color: var(--red); font-weight: 700; font-size: 32px; letter-spacing: 0.3px; line-height: 1;
  }
  .details__role { font-size: 17px; margin-top: 10px; letter-spacing: 0.3px; }
  .details__address { font-size: 17px; line-height: 27px; margin-top: 16px; letter-spacing: 0.3px; }
  .contact-list { list-style: none; margin-top: 15px; }
  .contact-list li {
    display: flex; align-items: center; gap: 9px;
    font-size: 17.4px; height: 27px; letter-spacing: 0.3px;
  }
  .contact-list svg { width: 16px; height: 16px; flex: none; fill: var(--red); }
</style>
</head>
<body>

<section class="card card--cover">
  <p class="tagline">Your SOLUTION to all of your Handyman and Home Improvement needs</p>
  <div class="wordmark">
    <span class="wordmark__dot"></span>
    <span>Marlow Estate<br>Services</span>
  </div>
  <p class="motto">Family Owned and Operated</p>
</section>

<section class="card card--contact">
  <div class="wordmark">
    <span class="wordmark__dot"></span>
    <span>Marlow Estate<br>Services</span>
  </div>
  <span class="divider"></span>
  <div class="details">
    <h1 class="details__name">DANIEL HARPER</h1>
    <p class="details__role">Managing Director</p>
    <p class="details__address">Your address, City<br>State, Zip 1234</p>
    <ul class="contact-list">
      <li>
        <svg viewBox="0 0 16 16" aria-hidden="true"><path d="M4 0h8a1.5 1.5 0 0 1 1.5 1.5v13A1.5 1.5 0 0 1 12 16H4a1.5 1.5 0 0 1-1.5-1.5v-13A1.5 1.5 0 0 1 4 0zm0 2v11h8V2zm4 11.6a.9.9 0 1 0 0 1.8.9.9 0 0 0 0-1.8z"/></svg>
        123 456 789
      </li>
      <li>
        <svg viewBox="0 0 16 16" aria-hidden="true"><path d="M1 5c1-2 4-3 7-3s6 1 7 3l-.5 2h-3l-.5-2H5l-.5 2h-3zM4 8h8l2 6H2zm4 1.5a2 2 0 1 0 0 4 2 2 0 0 0 0-4z"/></svg>
        123 456 789
      </li>
      <li>
        <svg viewBox="0 0 16 16" aria-hidden="true"><path d="M0 3h16v10H0zm1.5 1.5v.4L8 9l6.5-4.1v-.4zm0 2.2V11.5h13V6.7L8 10.8z"/></svg>
        info@marlowestateservices.com
      </li>
      <li>
        <svg viewBox="0 0 16 16" aria-hidden="true"><path d="M8 0a8 8 0 1 0 0 16A8 8 0 0 0 8 0zm-1 2.2c-.6.8-1.5 1-1.7 2 .6.7 1.8.3 2.3 1.2-.4 1-1.8.8-2.2 1.9.3 1 1.6 1 1.8 2.2l-.6 4.4A6 6 0 0 1 2.2 6C3.4 3.9 5 2.6 7 2.2zm3.5.6A6 6 0 0 1 14 8c-.6.8-1.6.5-2-.4-.7-1.3-2.4-.6-2.6-2.3-.1-1 .8-1.5 1.1-2.5z"/></svg>
        www.marlowestateservices.com
      </li>
    </ul>
  </div>
</section>

</body>
</html>
```